PPT :The Art Market in a changing world

Nr of Slides :19

To do
As I have no PDF Converter from PDF to PPT

1 All slides needs to be put in the LANDSCAPE format(horizontal)
2 I need to be able to change every picture /title (so no PDF)
3 Style & Color =Basic is red and white see slide 1
4 Every Title must be in a Red Block & White Letters
5 I need to be able to change every picture text in order to be able to update

-Slide 5 from the PDF : date 2016 needs to be 2018
-Slide 8. from the PDF :date 17 should be 2018
-Slide 9. from the PDF :date 2015 should be 2018

-Update by adding the latest related info

Target Market(s)

Art Professionals
Showing the power off the Mobile Phone /Computer /Platforms as a tool for the new art economy
Therefore I added some pictures of mobile phones ..

Font styles to use
Sans Serif

Colors
ec1f27
0255a3
ffffff

Requirements
Must have
• Attached files have the shade/tone of red I'd like you to use in the design.
• I need to be able to update every part of the slide (Title,date, picture,graph)
• Mention on the last slide my social media /logo plus account
• Flikora. Lucien Dramonte
• Workvine: Lucien Dramonte
• Chirply: DramonteLucien
Nice to have
• Possibility to insert a video (Flikora)

```html
<!DOCTYPE html>
<html lang="en">
<head>
<meta charset="UTF-8">
<title>The New Art Economy — Auction Houses Disrupted</title>
<link rel="stylesheet" href="https://fonts.googleapis.com/css2?family=Open+Sans:wght@400;700&display=swap">
<style>
  :root {
    --red-top: #e01010;
    --red-band: #cc0000;
    --ring: #9a0606;
    --photo-dark: #2e3a3a;
    --photo-mid: #6b7a7a;
    --white: #ffffff;
  }
  * { margin: 0; padding: 0; box-sizing: border-box; }
  html, body {
    width: 1200px;
    height: 900px;
    overflow: hidden;
  }
  body {
    font-family: "Open Sans", Arial, sans-serif;
    color: var(--white);
  }
  .slide {
    width: 1200px;
    height: 900px;
    position: relative;
    background: var(--red-top);
  }
  .profile {
    position: absolute;
    left: 0;
    top: 0;
    width: 1200px;
    height: 593px;
  }
  .portrait {
    position: absolute;
    left: 419px;
    top: 120px;
    width: 362px;
    height: 362px;
    border-radius: 50%;
    border: 4px solid var(--ring);
    background: radial-gradient(circle at 55% 40%, var(--photo-mid) 0%, var(--photo-dark) 75%);
  }
  .handle {
    position: absolute;
    left: 0;
    right: 0;
    top: 505px;
    display: flex;
    justify-content: center;
    align-items: center;
    gap: 14px;
    font-size: 30px;
    letter-spacing: 0.5px;
  }
  .handle-mark {
    width: 22px;
    height: 22px;
    border-radius: 50%;
    background: var(--white);
  }
  .title-band {
    position: absolute;
    left: 0;
    top: 593px;
    width: 1200px;
    height: 307px;
    background: var(--red-band);
    text-align: center;
    padding-top: 82px;
  }
  .title {
    font-size: 41px;
    font-weight: 700;
    line-height: 1.2;
  }
  .subtitle {
    font-size: 40px;
    font-weight: 400;
    line-height: 1.3;
    margin-top: 4px;
  }
</style>
</head>
<body>
  <main class="slide">
    <section class="profile">
      <div class="portrait" role="img" aria-label="Portrait photo of Lucien Dramonte"></div>
      <p class="handle"><span class="handle-mark" aria-hidden="true"></span><span>Chirply @DRAMONTELUCIEN</span></p>
    </section>
    <header class="title-band">
      <h1 class="title">THE NEW ART ECONOMY</h1>
      <p class="subtitle">AUCTION HOUSES DISRUPTED</p>
    </header>
  </main>
</body>
</html>
```